Security Warning Sign

We have an existing sign that needs an update. I have attached a picture of the current square sign. We need to maintain the same wording. It needs to be professional and appropriate to attach to our customers fence. Also attached is a copy of our building sign which may lend some inspiration and hopefully the ai format will assist. The final sign will be 600mm x 600mmOur website is www.halvorngate.com.au

```html
<!DOCTYPE html>
<html lang="en">
<head>
<meta charset="UTF-8">
<title>Security Warning Sign</title>
<link rel="stylesheet" href="https://fonts.googleapis.com/css2?family=Open+Sans:wdth,wght@75..100,400..800&display=swap">
<style>
  :root {
    --orange: #f28a24;
    --orange-deep: #e47a1c;
    --charcoal: #262626;
    --charcoal-deep: #151515;
    --white: #ffffff;
    --ink: #231f20;
    --page: #ffffff;
    --stripe-grey: #4a4a4a;
  }
  * { margin: 0; padding: 0; box-sizing: border-box; }
  html, body {
    width: 1200px;
    height: 700px;
    overflow: hidden;
    background: var(--page);
  }
  .canvas {
    position: relative;
    width: 1200px;
    height: 700px;
  }
  .sign {
    position: absolute;
    left: 300px;
    top: 50px;
    width: 600px;
    height: 600px;
    background: linear-gradient(160deg, var(--charcoal) 0%, #202020 55%, var(--charcoal-deep) 100%);
    box-shadow: 0 6px 14px rgba(0, 0, 0, 0.35);
    overflow: hidden;
    font-family: "Open Sans", Arial, sans-serif;
  }
  .sign__header {
    position: absolute;
    left: 0; top: 0;
    width: 600px;
    height: 131px;
    background: linear-gradient(150deg, var(--orange-deep) 0%, var(--orange) 45%, var(--orange-deep) 100%);
    display: flex;
    align-items: center;
    justify-content: center;
  }
  .sign__title {
    color: var(--ink);
    font-weight: 800;
    font-size: 104px;
    letter-spacing: 1px;
    line-height: 1;
    margin-top: 4px;
  }
  .sign__message {
    position: absolute;
    left: 0; top: 158px;
    width: 600px;
    text-align: center;
    color: var(--white);
    font-weight: 700;
    font-stretch: 75%;
    font-size: 56px;
    line-height: 63px;
    letter-spacing: 0.5px;
  }
  .brand {
    position: absolute;
    left: 20px;
    top: 496px;
    display: flex;
    align-items: center;
    gap: 12px;
  }
  .brand__dot {
    width: 70px;
    height: 70px;
    border-radius: 50%;
    background: var(--orange);
  }
  .brand__name {
    color: var(--white);
    font-weight: 800;
    font-size: 22px;
    line-height: 25px;
    letter-spacing: 0.5px;
  }
  .contact-bar {
    position: absolute;
    left: 368px;
    top: 504px;
  }
  .contact-bar__shape {
    position: absolute;
    left: -48px; top: 0;
  }
  .contact-bar__content {
    position: absolute;
    left: 0; top: 0;
    width: 232px;
    height: 56px;
    display: flex;
    align-items: center;
    gap: 8px;
    color: var(--white);
    font-weight: 800;
    font-stretch: 85%;
    font-size: 32px;
    letter-spacing: 0.3px;
  }
  .contact-bar__icon { flex: none; }
  .website {
    position: absolute;
    right: 22px;
    top: 571px;
    color: var(--white);
    font-weight: 800;
    font-size: 11.5px;
    letter-spacing: 0.3px;
  }
</style>
</head>
<body>
<div class="canvas">
  <section class="sign" aria-label="Security warning sign">
    <header class="sign__header">
      <h1 class="sign__title">WARNING</h1>
    </header>

    <p class="sign__message">
      ELECTRONIC<br>
      SURVEILLANCE<br>
      AND RECORDING<br>
      DEVICES INSTALLED<br>
      IN THIS AREA
    </p>

    <div class="brand">
      <span class="brand__dot"></span>
      <p class="brand__name">HALVORNGATE<br>SECURITY<br>SERVICES</p>
    </div>

    <div class="contact-bar">
      <svg class="contact-bar__shape" width="330" height="56" viewBox="0 0 330 56" aria-hidden="true">
        <polygon points="0,56 29,0 37,0 8,56" fill="var(--stripe-grey)"/>
        <polygon points="12,56 41,0 53,0 24,56" fill="var(--orange)"/>
        <polygon points="30,56 59,0 330,0 330,56" fill="var(--orange)"/>
      </svg>
      <div class="contact-bar__content">
        <svg class="contact-bar__icon" width="30" height="30" viewBox="0 0 24 24" aria-hidden="true">
          <path d="M6.6 10.8a15.1 15.1 0 0 0 6.6 6.6l2.2-2.2c.3-.3.7-.4 1-.2 1.1.4 2.3.6 3.6.6.6 0 1 .4 1 1V20c0 .6-.4 1-1 1C10.6 21 3 13.4 3 4c0-.6.4-1 1-1h3.5c.6 0 1 .4 1 1 0 1.3.2 2.5.6 3.6.1.3 0 .7-.2 1l-2.3 2.2z" fill="var(--white)"/>
          <path d="M14 3.5a7 7 0 0 1 6.5 6.5M14 6.5a4 4 0 0 1 3.5 3.5" stroke="var(--white)" stroke-width="1.6" fill="none" stroke-linecap="round"/>
        </svg>
        <span class="contact-bar__phone">1300 555 014</span>
      </div>
    </div>

    <p class="website">WWW.HALVORNGATE.COM.AU</p>
  </section>
</div>
</body>
</html>
```